Email Signature

We are looking for creative email signature for our company. Please find attached the logo of our company for your reference. now we understand there isn't much can be done with email signature but we are looking for out of the box designs. Nothing specific in mind

Please insert fake numbers, website and/or address, etc just to showcase the designs. once the design is chosen we will provide the actual details.
Updates

Dear All,

We wouldlike to extend our apology for not being able to provide feedbacks to everysingle design. We were extremely busy and we have multiple contests opensimultaneously which makes the process harder. However, thank you all for theefforts you have put into this contest. We have received anoverwhelming quality responses & it has been a very difficult task tochoose just one, we easily Loved at least several designs...

Thanksagain for participating, we wish you all success in your design ventures.

Kindregards,

HLW Team

Industry/Entity Type

It Company

```html
<!DOCTYPE html>
<html lang="en">
<head>
<meta charset="utf-8">
<title>HarborLantern Email Signature</title>
<link href="https://fonts.googleapis.com/css2?family=Source+Sans+3:wght@400;600;700&family=Roboto+Condensed:wght@700&display=swap" rel="stylesheet">
<style>
  :root {
    --ink: #1a1a1a;
    --accent-blue: #1c7fd6;
    --logo-blue: #2a8ee0;
    --tagline: #3a3a3a;
    --paper: #ffffff;
  }
  html, body {
    margin: 0;
    padding: 0;
    width: 1103px;
    height: 1200px;
    overflow: hidden;
    background: var(--paper);
  }
  .signature {
    position: relative;
    width: 1103px;
    height: 1200px;
    font-family: "Source Sans 3", "Myriad Pro", sans-serif;
    color: var(--ink);
  }
  .headline {
    position: absolute;
    left: 157px;
    top: 118px;
    margin: 0;
    font-size: 45px;
    font-weight: 400;
    line-height: 1;
  }
  .divider {
    position: absolute;
    left: 157px;
    top: 332px;
    width: 808px;
    height: 8px;
    background: var(--accent-blue);
  }
  .identity {
    position: absolute;
    left: 157px;
    top: 398px;
    margin: 0;
  }
  .identity .name {
    font-size: 36px;
    font-weight: 700;
    line-height: 40px;
    display: block;
  }
  .identity .role {
    font-size: 30px;
    line-height: 38px;
    display: block;
  }
  .contact {
    position: absolute;
    left: 157px;
    top: 562px;
    margin: 0;
    font-size: 34px;
    line-height: 45px;
    font-style: normal;
  }
  .contact .label {
    font-weight: 700;
  }
  .contact .email {
    color: var(--accent-blue);
    text-decoration: none;
  }
  .brand {
    position: absolute;
    left: 157px;
    top: 790px;
    display: flex;
    align-items: center;
    gap: 22px;
  }
  .brand-mark {
    width: 64px;
    height: 64px;
    border-radius: 50%;
    background: var(--logo-blue);
  }
  .brand-name {
    font-size: 84px;
    font-weight: 700;
    line-height: 1;
    color: var(--logo-blue);
  }
  .tagline {
    position: absolute;
    left: 157px;
    top: 1038px;
    margin: 0;
    font-family: "Roboto Condensed", "Arial Narrow", sans-serif;
    font-weight: 700;
    font-size: 30px;
    color: var(--tagline);
  }
</style>
</head>
<body>
  <div class="signature">
    <p class="headline">your text goes here</p>
    <div class="divider"></div>

    <p class="identity">
      <span class="name">Marcus T. Delaney , CPA.</span>
      <span class="role">Executive Vice President</span>
      <span class="role">Chief Bussines and Finance Officer</span>
    </p>

    <address class="contact">
      48 Quayside Ave. Port Avery, TX 77410 - 0318<br>
      <span class="label">P</span> 409.555.0142 <span class="label">M</span> 409.555.0187<br>
      <span class="label">F</span> 409.555.0163 <span class="label">E</span> <a class="email" href="mailto:hello@harborlantern.net">hello@harborlantern.net</a>
    </address>

    <div class="brand">
      <span class="brand-mark"></span>
      <span class="brand-name">HarborLantern</span>
    </div>

    <p class="tagline">Make Bussines Best With The HarborLantern “</p>
  </div>
</body>
</html>
```